QOR Exterior Coatings

double sided. the front i want the name of the business each word on a new line with the QOR being bigger. id like teal, black and white colors. the back i want my contact info. Flat, no gloss. Something professional and I want to feel the letters bump put of the card. if possible maybe a paint sprayer in corner. not a car paint spray. (no tank on top of gun)
no vehicle paint sprayers. that means no tank on top of the gun. doesn't have to have a sprayer. black/dark background on the front. white back ground on back with info

```html
<!DOCTYPE html>
<html lang="en">
<head>
<meta charset="UTF-8">
<title>QOR Exterior Coatings – Business Card</title>
<link rel="stylesheet" href="https://fonts.googleapis.com/css2?family=Oswald:wght@600&family=Montserrat:wght@700&family=Arimo:wght@400&display=swap">
<style>
  :root {
    --bg: #2a2a2c;
    --teal: #1a9a9c;
    --teal-bright: #1fa7a8;
    --ink: #0d0d0d;
    --paper: #ffffff;
    --muted: #1b1b1b;
  }
  * { margin: 0; padding: 0; box-sizing: border-box; }
  html, body {
    width: 1200px; height: 900px; overflow: hidden;
    background: var(--bg);
  }
  .canvas { position: relative; width: 1200px; height: 900px; }

  .card {
    position: absolute;
    width: 760px; height: 434px;
    border-radius: 34px;
    overflow: hidden;
  }

  /* Front face */
  .card-front {
    left: 60px; top: 30px;
    background: linear-gradient(35deg, #000 0%, #03181a 40%, #0b5e60 75%, var(--teal) 100%);
  }
  .front-logo {
    position: absolute; inset: 0;
    display: flex; flex-direction: column; align-items: center; justify-content: center;
    font-family: 'Oswald', sans-serif; font-weight: 600;
    color: var(--paper); text-transform: uppercase; line-height: 1;
  }
  .front-logo .mark-name { font-size: 150px; letter-spacing: 6px; }
  .front-logo .mark-sub { font-size: 44px; letter-spacing: 3px; margin-top: 12px; }

  /* Back face */
  .card-back {
    left: 380px; top: 440px;
    background: var(--paper);
  }
  .back-logo {
    position: absolute; left: 0; right: 0; top: 42px;
    display: flex; flex-direction: column; align-items: center;
    font-family: 'Oswald', sans-serif; font-weight: 600;
    color: var(--ink); text-transform: uppercase; line-height: 1;
  }
  .back-logo .mark-name { font-size: 92px; letter-spacing: 4px; }
  .back-logo .mark-sub { font-size: 30px; letter-spacing: 2px; margin-top: 6px; }

  .person {
    position: absolute; right: 430px; top: 254px;
    text-align: right;
  }
  .person .name {
    font-family: 'Montserrat', sans-serif; font-weight: 700;
    font-size: 31px; color: var(--teal); letter-spacing: 0.5px;
  }
  .person .role {
    font-family: 'Arimo', sans-serif; font-size: 20px; color: var(--muted);
    margin-top: 2px;
  }

  .divider {
    position: absolute; left: 350px; top: 250px;
    width: 2px; height: 76px; background: var(--ink);
  }

  .contacts {
    position: absolute; left: 374px; top: 246px;
    list-style: none;
    font-family: 'Arimo', sans-serif; font-size: 20px; color: var(--muted);
  }
  .contacts li { display: flex; align-items: center; gap: 10px; height: 28px; }
  .contacts svg { width: 18px; height: 18px; flex: none; fill: var(--teal); }

  .address {
    position: absolute; left: 0; right: 0; top: 366px;
    text-align: center;
    font-family: 'Arimo', sans-serif; font-size: 22px; color: var(--ink);
  }
</style>
</head>
<body>
<main class="canvas">

  <section class="card card-front" aria-label="Card front">
    <div class="front-logo">
      <span class="mark-name">QOR</span>
      <span class="mark-sub">Exterior Coatings</span>
    </div>
  </section>

  <section class="card card-back" aria-label="Card back">
    <div class="back-logo">
      <span class="mark-name">QOR</span>
      <span class="mark-sub">Exterior Coatings</span>
    </div>

    <div class="person">
      <div class="name">DANIEL REEVE</div>
      <div class="role">Manager</div>
    </div>

    <div class="divider"></div>

    <ul class="contacts">
      <li>
        <svg viewBox="0 0 24 24" aria-hidden="true"><path d="M6.6 10.8a15.1 15.1 0 0 0 6.6 6.6l2.2-2.2a1 1 0 0 1 1-.25 11.4 11.4 0 0 0 3.6.57 1 1 0 0 1 1 1V20a1 1 0 0 1-1 1A17 17 0 0 1 3 4a1 1 0 0 1 1-1h3.5a1 1 0 0 1 1 1c0 1.25.2 2.45.57 3.57a1 1 0 0 1-.25 1z"/></svg>
        <span>123-456-2100</span>
      </li>
      <li>
        <svg viewBox="0 0 24 24" aria-hidden="true"><path d="M2 5h20v14H2z M2 5l10 8 10-8" fill="none" stroke="#1a9a9c" stroke-width="2.4"/></svg>
        <span>youremail@mailbox.com</span>
      </li>
      <li>
        <svg viewBox="0 0 24 24" aria-hidden="true"><g fill="none" stroke="#1a9a9c" stroke-width="2.2"><circle cx="12" cy="12" r="9.5"/><ellipse cx="12" cy="12" rx="4" ry="9.5"/><path d="M2.5 12h19"/></g></svg>
        <span>www.yourwebsite.com</span>
      </li>
    </ul>

    <p class="address">Your address, city, state, ZIP 0000</p>
  </section>

</main>
</body>
</html>
```